Bref créative
Bellquist law p.a.
See logo attached
Simple
Hal Bellquist
Board Certified Trial Lawyer
Post Office Box 48716
27 West Caldera Street
Dunmore Bay, Calverton. 30874
Hal@bellquistlegal.example
Www.halbellquist.example
Here is a version with a slight varation in the size of bellquist law
Here is the final version of the logo with the bellquist law text included with the font that I though was most suitable. There is a white outline on this version that is not on the final version. It is a tif file that will not upload to this server but is on my facebook page. I can email it privately if someone needs it. I think this logo may look better on grey paper. The black background that I have in this attachment may not be feasible since it would require three colors on the letterhead. Anyway, thanks for your help.

```html
<!DOCTYPE html>
<html lang="en">
<head>
<meta charset="utf-8">
<title>Bellquist Law, P.A. — Stationery</title>
<link rel="stylesheet" href="https://fonts.googleapis.com/css2?family=Source+Sans+3:wght@400;600&display=swap">
<style>
  :root {
    --bg: #e9e9e9;
    --paper: #ffffff;
    --card-grey: #c9c9c9;
    --window: #ececec;
    --window-edge: #d4d4d4;
    --ink: #5a5a5a;
    --ink-soft: #8a8a8a;
    --accent: #e8731f;
    --edge: #d8d8d8;
  }
  * { box-sizing: border-box; margin: 0; padding: 0; }
  html, body { width: 1200px; height: 847px; overflow: hidden; }
  body {
    background: var(--bg);
    font-family: "Source Sans 3", "Myriad Pro", sans-serif;
    color: var(--ink);
    position: relative;
  }
  .sheet {
    position: absolute;
    background: var(--paper);
    border: 1px solid var(--edge);
  }
  address { font-style: normal; }

  /* brand mark: name set in text font with a plain square */
  .brand {
    display: flex;
    align-items: center;
    gap: 7px;
    color: var(--accent);
    font-weight: 600;
    white-space: nowrap;
  }
  .brand-square {
    width: 11px; height: 11px;
    background: var(--accent);
    flex: none;
  }

  .contact { font-size: 9px; line-height: 1.45; color: var(--ink); white-space: nowrap; }

  /* letterhead */
  .letterhead { left: 50px; top: 50px; width: 560px; height: 725px; }
  .letterhead .contact { position: absolute; left: 48px; top: 42px; }
  .letterhead .brand { position: absolute; left: 290px; top: 58px; font-size: 17px; }
  .letterhead .web {
    position: absolute; left: 0; right: 0; bottom: 30px;
    text-align: center; font-size: 10px; letter-spacing: 4px; color: var(--ink-soft);
  }

  /* envelope front */
  .envelope-front { left: 650px; top: 50px; width: 500px; height: 217px; }
  .envelope-front .brand { position: absolute; left: 26px; top: 28px; font-size: 15px; }
  .envelope-front .window {
    position: absolute; left: 26px; top: 88px; width: 188px; height: 62px;
    background: var(--window); border: 1px solid var(--window-edge); border-radius: 6px;
  }
  .envelope-front .return-line {
    position: absolute; left: 26px; bottom: 16px; font-size: 8.5px; color: var(--ink); white-space: nowrap;
  }

  /* envelope back */
  .envelope-back { left: 650px; top: 510px; width: 500px; height: 217px; }
  .envelope-back svg { position: absolute; inset: 0; }
  .envelope-back .web {
    position: absolute; left: 0; right: 0; top: 28px;
    text-align: center; font-size: 10px; letter-spacing: 3px; color: var(--ink-soft);
  }

  /* business cards */
  .card { width: 240px; height: 137px; top: 320px; }
  .card-front { left: 650px; background: var(--card-grey); border-color: #b8b8b8; }
  .card-front .brand { position: absolute; left: 62px; top: 48px; font-size: 14px; }
  .card-front .web {
    position: absolute; left: 62px; top: 72px; font-size: 8.5px; color: #ffffff; letter-spacing: 0.5px;
  }
  .card-back { left: 910px; }
  .card-back .brand { position: absolute; right: 14px; top: 18px; font-size: 10px; gap: 5px; }
  .card-back .brand-square { width: 8px; height: 8px; }
  .card-back .name { position: absolute; left: 14px; top: 16px; font-size: 11px; font-weight: 600; }
  .card-back .title { position: absolute; left: 14px; top: 30px; font-size: 7px; color: var(--ink-soft); }
  .card-back .contact { position: absolute; left: 14px; top: 76px; font-size: 7px; line-height: 1.4; }
</style>
</head>
<body>

  <section class="sheet letterhead" aria-label="Letterhead">
    <address class="contact">
      Post Office Box 48716<br>
      27 West Caldera Street<br>
      Dunmore Bay, Calverton. 30874<br>
      P 850 555 0142 | 850 555 0187<br>
      F 850 555 0193 | Email Hal@bellquistlegal.example
    </address>
    <div class="brand"><span class="brand-square"></span>Bellquist Law, P.A.</div>
    <div class="web">www.halbellquist.example</div>
  </section>

  <section class="sheet envelope-front" aria-label="Envelope front">
    <div class="brand"><span class="brand-square"></span>Bellquist Law, P.A.</div>
    <div class="window"></div>
    <div class="return-line">Post Office Box 48716 | 27 West Caldera Street | Dunmore Bay, Calverton. 30874</div>
  </section>

  <section class="sheet envelope-back" aria-label="Envelope back">
    <svg width="500" height="217" viewBox="0 0 500 217">
      <path d="M0 0 L250 110 L500 0" fill="none" stroke="#d0d0d0" stroke-width="1"/>
    </svg>
    <div class="web">www.halbellquist.example</div>
  </section>

  <section class="sheet card card-front" aria-label="Business card front">
    <div class="brand"><span class="brand-square"></span>Bellquist Law, P.A.</div>
    <div class="web">www.halbellquist.example</div>
  </section>

  <section class="sheet card card-back" aria-label="Business card back">
    <div class="name">Hal Bellquist</div>
    <div class="title">Board Certified Trial Lawyer</div>
    <div class="brand"><span class="brand-square"></span>Bellquist Law</div>
    <address class="contact">
      Post Office Box 48716<br>
      27 West Caldera Street<br>
      Dunmore Bay, Calverton. 30874<br>
      P 850 555 0142 | F 850 555 0193 | Hal@bellquistlegal.example
    </address>
  </section>

</body>
</html>
```